need a clean, modern job advertisement designed for social media (Facebook & Instagram).

The post is to advertise two positions:
• Leading Hand Boilermaker
• Dragline Fitter
We want the design to match our KRT Plant Services branding: blue, white, strong, professional, mining-industry style.
What the design should include:
Bold headline: “WE’RE HIRING”
Sub-headline: “Leading Hand Boilermaker & Dragline Fitter”
Key points:
• Bowen Basin based
• Dragline & shovel maintenance
• Great pay + long-term work
• Locally owned & operated
KRT logo placed cleanly
Space for 1–2 images (boilermaking or dragline work)
Design style:
Strong and industrial
Blue/white colour scheme
Easy to read at a glance
Suitable for a square 1080×1080 design

```html
<!DOCTYPE html>
<html lang="en">
<head>
<meta charset="utf-8">
<title>KRT Plant Services – We're Hiring</title>
<link rel="stylesheet" href="https://fonts.googleapis.com/css2?family=Archivo:wdth,wght@62..125,900&family=Rubik:wght@500;700;800&display=swap">
<style>
  :root{
    --bg-dark:#141212;
    --bg-band:#1c1c1e;
    --blue:#1a9ff0;
    --blue-deep:#0b6fd6;
    --cyan:#2ed8ef;
    --white:#ffffff;
    --ink:#0e1b2c;
    --steel:#c9cbce;
  }
  *{box-sizing:border-box;margin:0;padding:0}
  html,body{width:1200px;height:1200px;overflow:hidden;background:var(--bg-dark)}
  .post{
    position:relative;width:1200px;height:1200px;overflow:hidden;
    background:linear-gradient(180deg,#161413 0%,#120f0d 70%,#1a1a1b 100%);
    font-family:"Rubik",sans-serif;color:var(--white);
  }
  .hero-photo{
    position:absolute;left:560px;top:0;width:640px;height:700px;
    background:
      radial-gradient(circle at 72% 46%,rgba(190,220,255,.9) 0,rgba(60,110,230,.55) 9%,rgba(30,50,120,.25) 24%,transparent 40%),
      radial-gradient(circle at 52% 52%,rgba(140,40,40,.5) 0,transparent 30%),
      linear-gradient(160deg,#2a2d3a 0%,#1b1d27 45%,#231a16 100%);
  }
  .hero-photo::after{
    content:"";position:absolute;inset:0;
    background:linear-gradient(90deg,var(--bg-dark) 0%,rgba(20,18,18,0) 35%),
               linear-gradient(0deg,#120f0d 0%,rgba(18,15,13,0) 30%);
  }
  .brand{
    position:absolute;left:95px;top:140px;display:flex;align-items:center;gap:14px;
    font-weight:800;font-size:34px;letter-spacing:.5px;color:var(--white);
  }
  .brand-dot{width:30px;height:30px;border-radius:50%;background:var(--blue)}
  .tag-were{
    position:absolute;left:85px;top:265px;width:316px;height:92px;
    background:var(--blue);border-radius:12px;
    font-family:"Archivo",sans-serif;font-weight:900;font-stretch:88%;
    font-size:84px;line-height:92px;padding-left:14px;color:var(--white);
  }
  .tag-were::after{
    content:"";position:absolute;right:18px;bottom:-28px;
    border-left:10px solid transparent;border-right:6px solid var(--blue-deep);
    border-top:30px solid var(--blue-deep);
  }
  .headline{
    position:absolute;left:82px;top:350px;white-space:nowrap;
    font-family:"Archivo",sans-serif;font-weight:900;font-stretch:62%;
    font-size:232px;line-height:1;letter-spacing:-3px;
    transform:scaleX(.84);transform-origin:left top;
    background:linear-gradient(180deg,#ffffff 0%,#ffffff 52%,#d4d6d9 54%,#bfc1c4 100%);
    -webkit-background-clip:text;background-clip:text;color:transparent;
  }
  .roles{
    position:absolute;left:100px;top:598px;font-weight:700;font-size:45px;letter-spacing:.2px;white-space:nowrap;
  }
  .roles .accent{color:var(--cyan)}
  .location{
    position:absolute;left:100px;top:738px;font-weight:700;font-size:53px;
  }
  .perks{position:absolute;left:100px;top:822px;list-style:none}
  .perk{
    width:596px;height:52px;margin-bottom:13px;border-radius:10px;
    background:linear-gradient(90deg,var(--blue) 0%,#1689d8 55%,rgba(20,60,110,.35) 100%);
    display:flex;align-items:center;gap:12px;padding-left:10px;
    font-weight:700;font-size:33px;white-space:nowrap;
  }
  .tick{width:22px;height:22px;flex:none}
  .work-photos{position:absolute;left:700px;top:768px;display:flex;gap:14px}
  .work-photo{width:212px;height:222px;border:4px solid var(--white)}
  .work-photo.crew{background:linear-gradient(170deg,#8d959c 0%,#5c5f60 45%,#3a3a36 100%)}
  .work-photo.welder{background:linear-gradient(160deg,#3a3935 0%,#2a2622 50%,#5a4530 100%)}
  .cta-band{position:absolute;left:0;top:1035px;width:1200px;height:165px;background:var(--bg-band)}
  .cta-text{position:absolute;left:98px;top:1057px;font-weight:700;font-size:34.5px;white-space:nowrap}
  .cta-pill{
    position:absolute;left:651px;top:1057px;width:481px;height:51px;border-radius:10px;
    background:var(--blue);display:flex;align-items:center;padding-left:14px;gap:10px;overflow:hidden;
  }
  .cta-label{color:var(--ink);font-weight:500;font-size:26px;margin-right:12px}
  .cta-mail{width:30px;height:30px;flex:none}
  .cta-email{font-weight:700;font-size:28px;color:var(--white);white-space:nowrap}
</style>
</head>
<body>
<main class="post">
  <div class="hero-photo" role="img" aria-label="Boilermaker welding a steel pipe with a bright blue arc in a workshop"></div>

  <div class="brand"><span class="brand-dot"></span>KRT Plant Services</div>

  <div class="tag-were">WE’RE</div>
  <h1 class="headline">HIRING</h1>

  <p class="roles">Leading Hand <span class="accent">Boilermaker</span> &amp; <span class="accent">Dragline Fitter</span></p>

  <p class="location">Bowen Basin based</p>

  <ul class="perks">
    <li class="perk"><svg class="tick" viewBox="0 0 22 22"><circle cx="11" cy="11" r="10" fill="#0e1b2c"/><path d="M6.5 11.3l3 3 6-6.2" fill="none" stroke="#fff" stroke-width="2.4" stroke-linecap="round" stroke-linejoin="round"/></svg>Dragline &amp; shovel maintenance</li>
    <li class="perk"><svg class="tick" viewBox="0 0 22 22"><circle cx="11" cy="11" r="10" fill="#0e1b2c"/><path d="M6.5 11.3l3 3 6-6.2" fill="none" stroke="#fff" stroke-width="2.4" stroke-linecap="round" stroke-linejoin="round"/></svg>Great pay + long-term work</li>
    <li class="perk"><svg class="tick" viewBox="0 0 22 22"><circle cx="11" cy="11" r="10" fill="#0e1b2c"/><path d="M6.5 11.3l3 3 6-6.2" fill="none" stroke="#fff" stroke-width="2.4" stroke-linecap="round" stroke-linejoin="round"/></svg>Locally owned &amp; operated</li>
  </ul>

  <div class="work-photos">
    <div class="work-photo crew" role="img" aria-label="Maintenance crew in hi-vis working on a dragline boom on scaffolding"></div>
    <div class="work-photo welder" role="img" aria-label="Tradesman in hi-vis welding inside a dragline structure"></div>
  </div>

  <div class="cta-band"></div>
  <p class="cta-text">APPLY NOW or find out more by</p>
  <div class="cta-pill">
    <span class="cta-label">emailing</span>
    <svg class="cta-mail" viewBox="0 0 30 30"><rect x="3" y="9" width="24" height="17" rx="2" fill="#0e1b2c"/><path d="M3 11l12 8 12-8" fill="none" stroke="#1a9ff0" stroke-width="2"/><path d="M10 9V4h10v5" fill="none" stroke="#0e1b2c" stroke-width="2.2"/></svg>
    <span class="cta-email">admin@krt.net.au</span>
  </div>
</main>
</body>
</html>
```